Business card design for a dynamic IT consulting company

We need a business card design for a young firm, specialized in the Telecommunications/Consulting industry. The name of the company is Brask and Partners Business Consulting Ltd. (Short name: Brask and Partnes)
Brask = solve read reverse, so we aim to be uncomplicated and solution-oriented. The small pipe in our logo is also related to the word solve. So we need a new business card design, which is simple, eye catching and something non traditional (I would probably prefer a square shaped design rather than a rectangle, but open for suggestions). Attached our logo.

Target Market(s)

Usually our customers are Tier1 Telecoms providers (Q-Linkra, Parnexo, etc) and their executives.

Industry/Entity Type

Business

Contact Information for Business Card

Name: Gergely Halmindo
Email: g.halmindo@braskpartnera.hu
Web: www.braskpartnera.hu
Mobile: +36 30 555 0192
Title: Managing Director

Optional:
Company name: Brask and Partners Ltd.
Address: 1047 Budapest, Ravaszi str. 17/B, Hungary

Font styles to use
Other font styles liked:
• helveticaneue_medium, Prime Regular are used now.

Colors

Designer to choose colors to be used in the design.

Requirements
Must have
• I would like to have a 2 sided design.
Nice to have
• I thought if we make the logo a bit bigger (without the company name), that could go to the back with the company name below. I though, if the pipe in the logo is somehow touchable on the business card, would be nice and unique.

```html
<!DOCTYPE html>
<html lang="en">
<head>
<meta charset="utf-8">
<title>Brask and Partners – Business Card</title>
<link href="https://fonts.googleapis.com/css2?family=Roboto:wght@300;400;500&display=swap" rel="stylesheet">
<style>
  :root {
    --page-bg: #dedede;
    --card-bg: #ffffff;
    --card-tint: #f7f7f7;
    --ink: #4a4a4d;
    --ink-soft: #5c5c60;
    --accent-blue: #1a93d6;
    --accent-magenta: #c2187f;
    --rule: #6a6a6e;
  }
  * { margin: 0; padding: 0; box-sizing: border-box; }
  html, body {
    width: 1200px; height: 1200px; overflow: hidden;
    background: var(--page-bg);
    font-family: "Roboto", Arial, sans-serif;
    color: var(--ink);
  }
  .stage { position: relative; width: 1200px; height: 1200px; }
  .card {
    position: absolute; top: 437px;
    width: 480px; height: 270px;
    background: var(--card-bg);
    overflow: hidden;
  }
  .card--front { left: 66px; }
  .card--back { left: 652px; }
  .card-texture {
    position: absolute; inset: 0;
    background: radial-gradient(ellipse at 50% 50%, var(--card-bg) 35%, var(--card-tint) 100%);
  }
  .brand {
    position: absolute; left: 0; right: 0;
    display: flex; align-items: center; justify-content: center; gap: 10px;
  }
  .brand-mark { width: 12px; height: 12px; background: var(--accent-blue); }
  .brand-name { font-weight: 300; color: var(--ink); letter-spacing: 0.2px; white-space: nowrap; }
  .card--front .brand { top: 112px; }
  .card--front .brand-name { font-size: 30px; }
  .card--back .brand { top: 76px; }
  .card--back .brand-name { font-size: 26px; }
  .person {
    position: absolute; top: 138px; right: 267px;
    text-align: right;
  }
  .person-name { font-size: 12px; font-weight: 400; color: var(--accent-blue); line-height: 16px; }
  .person-title { font-size: 9.5px; color: var(--ink-soft); line-height: 15px; }
  .divider {
    position: absolute; left: 229px; top: 134px;
    width: 1px; height: 62px; background: var(--rule);
  }
  .contacts {
    position: absolute; left: 243px; top: 137px;
    list-style: none; font-size: 9.5px; color: var(--ink); line-height: 13.5px;
  }
  .contacts li { display: flex; align-items: flex-start; gap: 6px; }
  .contacts svg { width: 9px; height: 9px; margin-top: 2px; flex: none; fill: var(--ink); }
</style>
</head>
<body>
<main class="stage">
  <section class="card card--front" aria-label="Card front">
    <div class="card-texture" role="img" aria-label="Faint diamond pattern background"></div>
    <div class="brand">
      <span class="brand-mark"></span>
      <span class="brand-name">Brask &amp; Partners</span>
    </div>
  </section>

  <section class="card card--back" aria-label="Card back">
    <div class="card-texture" role="img" aria-label="Faint diamond pattern background"></div>
    <div class="brand">
      <span class="brand-mark"></span>
      <span class="brand-name">Brask &amp; Partners</span>
    </div>
    <div class="person">
      <p class="person-name">Gergely Halmindo</p>
      <p class="person-title">Managing Director</p>
    </div>
    <div class="divider"></div>
    <ul class="contacts">
      <li><svg viewBox="0 0 10 10"><path d="M2 0.5 L3.6 2.6 L2.8 3.6 Q4 5.8 6.4 7.2 L7.4 6.4 L9.5 8 L8.4 9.5 Q3.6 9 0.5 1.6 Z"/></svg>+36 30 555 0192</li>
      <li><svg viewBox="0 0 10 10"><path d="M0.5 2 H9.5 V8.5 H0.5 Z M1.2 2.6 L5 5.4 L8.8 2.6 V3.5 L5 6.3 L1.2 3.5 Z" fill-rule="evenodd"/></svg>g.halmindo@braskpartnera.hu</li>
      <li><svg viewBox="0 0 10 10"><path d="M3 3 H5 V4 H3 A1 1 0 0 0 3 6 H5 V7 H3 A2 2 0 0 1 3 3 Z M5 3 H7 A2 2 0 0 1 7 7 H5 V6 H7 A1 1 0 0 0 7 4 H5 Z M3.5 4.6 H6.5 V5.4 H3.5 Z"/></svg>www.braskpartnera.hu</li>
      <li><svg viewBox="0 0 10 10"><path d="M5 0.5 A3.2 3.2 0 0 1 8.2 3.7 C8.2 6 5 9.5 5 9.5 C5 9.5 1.8 6 1.8 3.7 A3.2 3.2 0 0 1 5 0.5 Z M5 2.5 A1.2 1.2 0 1 0 5 4.9 A1.2 1.2 0 1 0 5 2.5 Z" fill-rule="evenodd"/></svg><span>1047 Budapest, Ravaszi<br>str. 17/B, Hungary</span></li>
    </ul>
  </section>
</main>
</body>
</html>
```